Bref créative
QDRL Stationary
Professional
Delvonte Ashby
CEO
4815 Marigold Ln
Alderton, TX 70000
dashby@qdrlinc.example
www.QDRLInc.example
My company Logo should be placed on the back of the card.

```html
<!DOCTYPE html>
<html lang="en">
<head>
<meta charset="UTF-8">
<title>QDRL Stationery — Business Card</title>
<link rel="stylesheet" href="https://fonts.googleapis.com/css2?family=Open+Sans:wght@400;600;800&display=swap">
<style>
  :root {
    --page: #ecebe7;
    --white: #ffffff;
    --green-light: #6cc335;
    --green: #3fa41c;
    --green-dark: #1f7a0e;
    --ink: #222222;
    --rule: #111111;
    --band: #c9c9c9;
  }
  * { margin: 0; padding: 0; box-sizing: border-box; }
  html, body { width: 1200px; height: 646px; overflow: hidden; }
  body {
    background: var(--page);
    font-family: "Open Sans", Arial, sans-serif;
    position: relative;
  }
  .card {
    position: absolute;
    top: 175px;
    width: 520px;
    height: 297px;
    overflow: hidden;
    box-shadow: 0 6px 18px rgba(0,0,0,.18);
  }
  .card-back {
    left: 50px;
    background: radial-gradient(ellipse at 45% 40%, var(--green-light) 0%, var(--green) 50%, var(--green-dark) 100%);
    display: flex; align-items: center; justify-content: center;
  }
  .card-front { left: 630px; background: var(--white); }
  .card-front .swoosh { position: absolute; inset: 0; width: 100%; height: 100%; }

  .brand { display: flex; flex-direction: column; align-items: center; gap: 8px; position: absolute; }
  .brand-dot { width: 34px; height: 34px; border-radius: 50%; }
  .brand-name { font-weight: 800; letter-spacing: 1px; line-height: 1; }
  .card-back .brand { position: static; }
  .card-back .brand-dot { background: var(--white); width: 46px; height: 46px; }
  .card-back .brand-name { color: var(--white); font-size: 56px; }
  .card-front .brand { left: 0; right: 0; top: 38px; }
  .card-front .brand-dot { background: var(--green); }
  .card-front .brand-name { color: var(--ink); font-size: 40px; }

  .person {
    position: absolute; left: 36px; top: 208px;
    color: var(--white); font-size: 10.5px; line-height: 1.45;
  }
  .person-name { font-weight: 600; font-size: 13px; }
  .person-title { margin-bottom: 8px; }

  .contacts {
    position: absolute; left: 338px; top: 160px;
    list-style: none; color: var(--white); font-size: 10px;
  }
  .contacts li { display: flex; align-items: center; gap: 7px; height: 19px; white-space: nowrap; }
  .contacts svg { width: 12px; height: 12px; flex: none; }
</style>
</head>
<body>

<section class="card card-back" aria-label="Card back">
  <div class="brand">
    <span class="brand-dot"></span>
    <span class="brand-name">QDRL</span>
  </div>
</section>

<section class="card card-front" aria-label="Card front">
  <svg class="swoosh" viewBox="0 0 520 297" preserveAspectRatio="none">
    <defs>
      <linearGradient id="greenFill" x1="0" y1="0" x2="1" y2="1">
        <stop offset="0" stop-color="var(--green-light)"/>
        <stop offset=".55" stop-color="var(--green)"/>
        <stop offset="1" stop-color="var(--green-dark)"/>
      </linearGradient>
    </defs>
    <path d="M0,168 C190,182 390,130 520,0 L520,297 L0,297Z" fill="var(--band)"/>
    <path d="M0,176 C190,190 395,140 520,8 L520,297 L0,297Z" fill="var(--rule)"/>
    <path d="M0,182 C195,196 400,146 520,16 L520,297 L0,297Z" fill="url(#greenFill)"/>
  </svg>

  <div class="brand">
    <span class="brand-dot"></span>
    <span class="brand-name">QDRL</span>
  </div>

  <div class="person">
    <p class="person-name">Delvonte Ashby</p>
    <p class="person-title">CEO</p>
    <p>4815 Marigold Ln</p>
    <p>Alderton, TX 70000</p>
  </div>

  <ul class="contacts">
    <li>
      <svg viewBox="0 0 12 12"><path d="M3 1h2l1 3-1.5 1a6 6 0 0 0 2.5 2.5L8 6l3 1v2a1.5 1.5 0 0 1-1.5 1.5A8.5 8.5 0 0 1 1.5 2.5 1.5 1.5 0 0 1 3 1z" fill="#fff"/></svg>
      (T) 555-014-2231
    </li>
    <li>
      <svg viewBox="0 0 12 12"><rect x="3" y="0.5" width="6" height="11" rx="1.2" fill="#fff"/><rect x="4" y="2" width="4" height="7" fill="var(--green)"/></svg>
      (C) 555-014-7780
    </li>
    <li>
      <svg viewBox="0 0 12 12"><rect x="1" y="4" width="10" height="6" rx="1" fill="#fff"/><rect x="3" y="1" width="6" height="3" fill="#fff"/></svg>
      (F) 555-014-9904
    </li>
    <li>
      <svg viewBox="0 0 12 12"><rect x="0.5" y="2" width="11" height="8" rx="1" fill="#fff"/><path d="M1 2.5l5 4 5-4" stroke="var(--green)" fill="none"/></svg>
      dashby@qdrlinc.example
    </li>
    <li>
      <svg viewBox="0 0 12 12"><circle cx="6" cy="6" r="5" stroke="#fff" fill="none"/><path d="M1 6h10M6 1c-3 3-3 7 0 10M6 1c3 3 3 7 0 10" stroke="#fff" fill="none"/></svg>
      www.QDRLInc.example
    </li>
  </ul>
</section>

</body>
</html>
```